Shopify Design for a Homeopathic Shop

The design should let the user give a feeling of luxury and naturality(earthy).

We want to build up a alternative medicine luxury brand. The user should have a feeling of trust when visiting our shop. We stand for natural remedies.

Target Market(s)

Alternative / Left

Industry/Entity Type

Alternative Medicine

Font styles to use
Sans Serif

Colors

Designer to choose colors to be used in the design.

```html
<!DOCTYPE html>
<html lang="en">
<head>
<meta charset="utf-8">
<title>Verdalis — Homeopathic Remedies</title>
<link href="https://fonts.googleapis.com/css2?family=Montserrat:wght@300;400;500&family=Open+Sans:wght@400;600&display=swap" rel="stylesheet">
<style>
:root{
  --olive:#7b7a3d;
  --ink:#2e2e2e;
  --muted:#6f6f6f;
  --line:#dcdcdc;
  --sage-band:#e5e7e2;
  --sand-band:#ede2cb;
  --footer:#3a2a1f;
  --footer-text:#e9e1d6;
  --white:#ffffff;
}
*{margin:0;padding:0;box-sizing:border-box}
html,body{width:1200px;height:5155px;overflow:hidden;background:var(--white)}
body{position:relative;font-family:'Open Sans',sans-serif;color:var(--ink)}
.abs{position:absolute}
.head{font-family:'Montserrat',sans-serif;font-weight:400;color:var(--ink)}
.btn{position:absolute;background:var(--olive);color:var(--white);font-family:'Montserrat',sans-serif;font-size:17px;display:flex;align-items:center;justify-content:center;letter-spacing:.5px}
.photo{position:absolute}
/* header */
.social-top{left:110px;top:44px;display:flex;gap:18px}
.social-top span{width:22px;height:22px;border-radius:4px;background:#777;display:block}
.brand{left:0;width:1200px;top:42px;text-align:center}
.brand .name{font-family:'Montserrat',sans-serif;font-size:42px;font-weight:400;letter-spacing:2px;color:#222}
.brand .tag{font-family:'Montserrat',sans-serif;font-size:10px;letter-spacing:7px;color:#444;margin-top:-4px}
.tools{right:110px;top:44px;display:flex;gap:20px}
.nav{left:0;width:1200px;top:126px;display:flex;justify-content:center;gap:46px;font-family:'Montserrat',sans-serif;font-size:16px;color:#333}
.rule{left:0;width:1200px;height:1px;background:var(--line)}
.perk{top:190px;display:flex;gap:20px;align-items:flex-start;font-size:15px}
.perk small{display:block;font-size:12px;color:var(--muted);margin-top:6px}
.perk a{color:var(--olive);font-size:12px;display:block;margin-top:6px;text-decoration:underline}
.vdiv{top:172px;width:1px;height:84px;background:var(--line)}
/* hero */
.hero-title{left:108px;top:366px;font-family:'Montserrat',sans-serif;font-weight:300;font-size:50px;line-height:68px;color:var(--white);letter-spacing:1px}
.dots{left:558px;top:728px;display:flex;gap:8px}
.dots i{width:14px;height:14px;border-radius:50%;border:2px solid #fff;display:block}
.dots i:first-child{background:#fff}
.sec-title{left:0;width:1200px;text-align:center;font-size:38px}
.card-img{background:#f0ede7}
.sale{background:var(--olive);color:#fff;font-size:15px;padding:6px 14px;font-family:'Montserrat',sans-serif}
.prod-name{text-align:center;font-family:'Montserrat',sans-serif;font-size:20px}
.price{text-align:center;font-size:14px;color:var(--muted)}
.price s{color:#555}
.body-text{font-size:13.5px;line-height:30px;color:#555}
.blog-box{background:#fff;box-shadow:0 2px 10px rgba(0,0,0,.12);text-align:center;padding-top:28px}
.blog-box h3{font-family:'Montserrat',sans-serif;font-weight:400;font-size:18px;line-height:29px;color:#333}
.blog-box p{font-size:13px;color:#666;margin-top:14px}
.foot h4{font-family:'Montserrat',sans-serif;font-weight:400;font-size:19px;color:#fff}
.foot p,.foot li{font-size:12.5px;line-height:26px;color:var(--footer-text);list-style:none}
.foot li{line-height:33px}
</style>
</head>
<body>

<!-- header -->
<div class="abs social-top" aria-label="Social links"><span></span><span></span><span></span></div>
<div class="abs brand">
  <div class="name">VERDALIS</div>
  <div class="tag">HOMEOPATHIC REMEDIES</div>
</div>
<div class="abs tools">
  <svg width="22" height="22" viewBox="0 0 22 22" fill="none" stroke="#777" stroke-width="2"><circle cx="9" cy="9" r="7"/><path d="M14 14l6 6"/></svg>
  <svg width="22" height="22" viewBox="0 0 22 22" fill="none" stroke="#777" stroke-width="2"><circle cx="11" cy="7" r="5"/><path d="M2 21c1-6 17-6 18 0"/></svg>
  <svg width="26" height="22" viewBox="0 0 26 22" fill="none" stroke="#777" stroke-width="2"><path d="M1 2h4l3 13h14l3-10H7"/><circle cx="10" cy="19" r="2"/><circle cx="20" cy="19" r="2"/></svg>
</div>
<nav class="abs nav"><span>HOME</span><span>ABOUT</span><span>SHOP ▾</span><span>BLOG</span><span>FAQS</span><span>CONTACT</span></nav>
<div class="abs rule" style="top:171px"></div>

<div class="abs perk" style="left:110px">
  <svg width="34" height="28" viewBox="0 0 34 28"><rect x="1" y="6" width="20" height="14" fill="#8a6a4a"/><path d="M21 10h7l5 6v4H21z" fill="#8a6a4a"/><circle cx="8" cy="22" r="4" fill="#8a6a4a"/><circle cx="26" cy="22" r="4" fill="#8a6a4a"/></svg>
  <div>Free Delivery Worldwide<small>On order up to $1999</small></div>
</div>
<div class="abs vdiv" style="left:420px"></div>
<div class="abs perk" style="left:482px">
  <svg width="32" height="30" viewBox="0 0 32 30"><path d="M2 2h13l15 15-12 12L2 15z" fill="#8a6a4a"/><circle cx="9" cy="9" r="3" fill="#fff"/></svg>
  <div>Final Clearance Sale<small>Up to 30% off</small></div>
</div>
<div class="abs vdiv" style="left:776px"></div>
<div class="abs perk" style="left:846px">
  <svg width="30" height="30" viewBox="0 0 30 30"><circle cx="15" cy="15" r="11" fill="#8a6a4a"/><circle cx="15" cy="15" r="14" fill="none" stroke="#8a6a4a" stroke-width="3" stroke-dasharray="3 3"/></svg>
  <div>Get $10 Offer<a>On Your First Order!</a></div>
</div>
<div class="abs rule" style="top:255px"></div>

<!-- hero -->
<div class="photo" role="img" aria-label="Oil dropper bottles with green leaves on pale wooden boards" style="left:0;top:256px;width:1200px;height:556px;background:linear-gradient(100deg,#cfc8c0 0%,#d9d2c8 40%,#b7b07a 55%,#2f4f2e 75%,#cfc6bb 100%)"></div>
<div class="abs hero-title">HOMEOPATHIC<br>MEDICINES</div>
<div class="btn" style="left:110px;top:526px;width:170px;height:56px">SHOP NOW!</div>
<div class="abs dots"><i></i><i></i><i></i><i></i></div>

<!-- featured -->
<h2 class="abs head sec-title" style="top:910px">FEATURED PRODUCTS</h2>
<div class="photo card-img" role="img" aria-label="Remedy pill bottles with red labels" style="left:110px;top:1018px;width:312px;height:332px;background:linear-gradient(180deg,#f1eee8,#e6e2da)"></div>
<div class="abs sale" style="left:110px;top:1018px">SALE!</div>
<div class="photo card-img" role="img" aria-label="Amber capsule jar with green leaves" style="left:444px;top:1018px;width:288px;height:332px;background:linear-gradient(180deg,#f1eee8,#e3ddd3)"></div>
<div class="photo card-img" role="img" aria-label="Amber dropper bottle with red cap" style="left:774px;top:1018px;width:310px;height:332px;background:linear-gradient(180deg,#f1eee8,#e6e1d8)"></div>
<div class="abs sale" style="left:774px;top:1018px">SALE!</div>

<div class="abs prod-name" style="left:110px;width:312px;top:1384px">Finibus Bonoet Malo</div>
<div class="abs price" style="left:110px;width:312px;top:1422px"><s>$30.00</s> from $25.00</div>
<div class="abs prod-name" style="left:444px;width:312px;top:1384px">Finibus Bonoet Malo</div>
<div class="abs price" style="left:444px;width:312px;top:1422px"><s>$30.00</s> from $25.00</div>
<div class="abs prod-name" style="left:774px;width:312px;top:1384px">Finibus Bonoet Malo</div>
<div class="abs price" style="left:774px;width:312px;top:1422px"><s>$30.00</s> from $25.00</div>

<!-- brand band -->
<section class="abs" style="left:0;top:1550px;width:1200px;height:526px;background:var(--sage-band)"></section>
<div class="photo" role="img" aria-label="Herbal tablets and green leaves spilling from a glass jar" style="left:560px;top:1550px;width:640px;height:526px;background:radial-gradient(ellipse at 60% 50%,#d8d8c6 0%,#e5e7e2 70%)"></div>
<h2 class="abs head" style="left:108px;top:1638px;font-size:38px">VERDALIS</h2>
<p class="abs body-text" style="left:110px;top:1708px;width:420px">Nemo enim ipsam voluptatem quia voluptas sit aspernatur aut odit aut fugit, sed quia consequuntur magni dolores eos qui ratione voluptatem sequi nesciunt.</p>
<div class="btn" style="left:110px;top:1826px;width:170px;height:56px">SHOP NOW!</div>

<!-- about -->
<div class="abs" style="left:102px;top:2202px;width:4px;height:396px;background:var(--olive)"></div>
<div class="abs" style="left:102px;top:2594px;width:200px;height:4px;background:var(--olive)"></div>
<div class="photo" role="img" aria-label="Amber remedy bottles, dried herbs and white tablets on a reflective surface" style="left:112px;top:2190px;width:456px;height:400px;background:linear-gradient(180deg,#ddd8dd 0%,#e8e4e6 60%,#f3f1f2 100%)"></div>
<h2 class="abs head" style="left:640px;top:2220px;font-size:38px">ABOUT US</h2>
<p class="abs body-text" style="left:640px;top:2294px;width:450px">Neque porro quisquam est, qui dolorem ipsum quia dolor siamet, consectetur, adipisci velit, sed quia non numquam eius modi timp ora incidunt ut labore et dolore magnam aliquam quaerat volupta tem. Ut enim ad minima veniam, quis nostrum exercitationillam corporis suscipit laboriosam, nisi ut aliq.</p>
<div class="btn" style="left:640px;top:2494px;width:170px;height:56px">READ MORE</div>

<!-- gallery -->
<section class="abs" style="left:0;top:2700px;width:1200px;height:816px;background:var(--sand-band)"></section>
<div class="abs" style="left:384px;top:2794px;width:30px;height:30px;border:3px solid #333;border-radius:6px"></div>
<h2 class="abs head" style="left:434px;top:2786px;font-size:38px">WHAT WE'RE UP TO</h2>
<div class="photo" role="img" aria-label="Essential oil bottles with herbs" style="left:0;top:2898px;width:296px;height:268px;background:linear-gradient(135deg,#d6c27a,#5f7d3e)"></div>
<div class="photo" role="img" aria-label="Rows of white-capped remedy bottles" style="left:300px;top:2898px;width:296px;height:268px;background:linear-gradient(135deg,#d9d3c7,#4a3a2c)"></div>
<div class="photo" role="img" aria-label="Hands holding a natural medicine card with herbs" style="left:604px;top:2898px;width:296px;height:268px;background:linear-gradient(135deg,#c9b594,#6f7a4a)"></div>
<div class="photo" role="img" aria-label="Homeopathic globule tubes" style="left:904px;top:2898px;width:296px;height:268px;background:linear-gradient(135deg,#eef0ea,#8aa07c)"></div>
<div class="photo" role="img" aria-label="Fresh herbs with a capsule" style="left:0;top:3172px;width:296px;height:268px;background:linear-gradient(135deg,#f5f5f2,#4f7a34)"></div>
<div class="photo" role="img" aria-label="Corked pharmacy bottles" style="left:300px;top:3172px;width:296px;height:268px;background:linear-gradient(135deg,#8a6a4a,#1f2a3a)"></div>
<div class="photo" role="img" aria-label="Herbal tablets and leaves from a jar" style="left:604px;top:3172px;width:296px;height:268px;background:linear-gradient(135deg,#f0efe8,#b9b89a)"></div>
<div class="photo" role="img" aria-label="Amber bottle and mortar on wood" style="left:904px;top:3172px;width:296px;height:268px;background:linear-gradient(135deg,#3e2c3a,#8a6446)"></div>

<!-- blog -->
<h2 class="abs head sec-title" style="top:3614px">LATEST BLOG</h2>
<div class="photo" role="img" aria-label="Herbal oil and mortar with leaves" style="left:110px;top:3710px;width:316px;height:250px;background:linear-gradient(160deg,#e9e6d8,#c7b970)"></div>
<div class="photo" role="img" aria-label="Pharmacist preparing a remedy" style="left:442px;top:3710px;width:316px;height:250px;background:linear-gradient(160deg,#ebe8e4,#b9a690)"></div>
<div class="photo" role="img" aria-label="Amber dropper bottles with eucalyptus" style="left:774px;top:3710px;width:316px;height:250px;background:linear-gradient(160deg,#f1efea,#5a3a22)"></div>
<div class="abs blog-box" style="left:126px;top:3922px;width:286px;height:146px"><h3>Temporibus autem qubuset<br>aut officiis debitis aut</h3><p>▦ Wed, Oct 16 3pm ET</p></div>
<div class="abs blog-box" style="left:458px;top:3922px;width:286px;height:146px"><h3>Temporibus autem qubuset<br>aut officiis debitis aut</h3><p>▦ Wed, Oct 16 3pm ET</p></div>
<div class="abs blog-box" style="left:790px;top:3922px;width:286px;height:146px"><h3>Temporibus autem qubuset<br>aut officiis debitis aut</h3><p>▦ Wed, Oct 16 3pm ET</p></div>

<!-- video -->
<div class="photo" role="img" aria-label="Pharmacist mixing white powder in a bowl among bottles" style="left:0;top:4178px;width:1200px;height:522px;background:linear-gradient(100deg,#3b4a3e 0%,#b9b7b1 35%,#e4e2de 60%,#cfc9c2 100%)"></div>
<svg class="abs" style="left:564px;top:4406px" width="72" height="72" viewBox="0 0 72 72"><circle cx="36" cy="36" r="35" fill="#2a2a2a" fill-opacity=".85"/><path d="M29 23l21 13-21 13z" fill="#fff"/></svg>

<!-- footer -->
<footer class="abs foot" style="left:0;top:4700px;width:1200px;height:455px;background:var(--footer)">
  <h4 class="abs" style="left:110px;top:80px">About our store</h4>
  <p class="abs" style="left:110px;top:126px;width:310px">Nam libero tempore, cum soluta nobis est elige ndi optio cumque nihil impedit quo minus id qu od maxime placeat facere possimus, omnis volu ptas assumenda est, omnis.</p>
  <div class="abs" style="left:110px;top:232px;display:flex;gap:10px">
    <span style="width:64px;height:38px;background:#fff;border-radius:3px"></span>
    <span style="width:64px;height:38px;background:#fff;border-radius:3px"></span>
    <span style="width:64px;height:38px;background:#fff;border-radius:3px"></span>
    <span style="width:64px;height:38px;background:#fff;border-radius:3px"></span>
  </div>
  <h4 class="abs" style="left:468px;top:80px">Customer Service</h4>
  <ul class="abs" style="left:470px;top:118px">
    <li>Delivery Information</li><li>My Account</li><li>Order Tracking</li><li>Reminder Service</li><li>Shipping, Returns &amp; Fees</li>
  </ul>
  <h4 class="abs" style="left:726px;top:80px">Newsletter Subscription</h4>
  <p class="abs" style="left:728px;top:122px;width:300px">Register your Email Address to get information about us</p>
  <div class="abs" style="left:728px;top:218px;width:266px;height:44px;background:#fff;font-size:13px;color:#555;padding:13px 20px">Email Address</div>
  <div class="abs" style="left:994px;top:218px;width:94px;height:44px;background:var(--olive);color:#fff;font-size:13px;font-weight:600;display:flex;align-items:center;justify-content:center">SUBSCRIBE</div>
  <div class="abs" style="left:728px;top:274px;display:flex;gap:14px">
    <span style="width:42px;height:42px;border:1px solid #8a7a6a;border-radius:50%"></span>
    <span style="width:42px;height:42px;border:1px solid #8a7a6a;border-radius:50%"></span>
    <span style="width:42px;height:42px;border:1px solid #8a7a6a;border-radius:50%"></span>
    <span style="width:42px;height:42px;border:1px solid #8a7a6a;border-radius:50%"></span>
  </div>
  <p class="abs" style="left:0;width:1200px;top:392px;text-align:center;font-size:13px">Copyrights © 2019, Verdalis. All Rights Reserved.</p>
</footer>

</body>
</html>
```